Catchy Cards for Hospital

I run a rural hospital in Texas called Pellor Valley Hospital and am in need of contemporary business cards for all of my Department Heads. While our logo is somewhat simplistic, I don't have the option of changing it at this time, so anything to make the rest of the card present the appearance of a modern, professional healthcare facility would be great. Although the attached files are in black, our hospital colors are in a copper brown and black. I need to be able to change the name and title on the card so I can get cards printed for various department heads.

Target Market(s)

Referring physicians, large hospital systems, national organizations, state and federal government

Industry/Entity Type

Hospital

Contact Information for Business Card

Name Dale Hoskin
Title CEO

Phone: Main 555-321-0147 & Direct xxxxxx
Fax xxxxx
dale.hoskin@pellorvh.example
382 Wimble Street Box 415
Brannock, Westria 76902

Font styles to use
Serif

Colors
f48340

Requirements
Must have
• Clean crisp lines and ability to modify names, titles and emails
• On the back "PellorValleyHospital.Example
Nice to have
• Needs to be in line with logo, which is a bit dated and not too appealing, but I'm hoping that the rest of the card can make up for that fact just a little bit.
• Hospital's colors are a copper brown, black and white
Should not have
• Shapes or anything distracting

```html
<!DOCTYPE html>
<html lang="en">
<head>
<meta charset="utf-8">
<title>Pellor Valley Hospital — Business Card</title>
<link href="https://fonts.googleapis.com/css2?family=Lato:wght@400;700&display=swap" rel="stylesheet">
<style>
  :root {
    --orange: #f0691f;
    --orange-line: #f48340;
    --ink: #1b1b1b;
    --grey-text: #4a4a4a;
    --paper: #fbfbfa;
    --backdrop: #e6e6e4;
  }
  * { box-sizing: border-box; margin: 0; padding: 0; }
  html, body { width: 1200px; height: 1021px; overflow: hidden; }
  body {
    background: var(--backdrop);
    font-family: "Lato", Arial, sans-serif;
    position: relative;
  }
  .card {
    position: absolute;
    width: 700px;
    height: 400px;
    overflow: hidden;
    box-shadow: 0 6px 18px rgba(0,0,0,0.18);
  }
  .card-front { left: 110px; top: 60px; background: var(--paper); }
  .front-logo {
    position: absolute; right: 48px; top: 58px;
    color: var(--orange); font-weight: 700; font-size: 28px;
    letter-spacing: 0.3px;
  }
  .rule-orange {
    position: absolute; left: 400px; right: 0; top: 112px;
    height: 3px; background: var(--orange-line);
  }
  .rule-black {
    position: absolute; left: 0; width: 400px; top: 160px;
    height: 2px; background: var(--ink);
  }
  .person { position: absolute; left: 40px; top: 100px; padding-left: 14px; }
  .person::before {
    content: ""; position: absolute; left: 0; top: 4px;
    width: 6px; height: 46px; background: var(--orange);
  }
  .person-name { font-size: 26px; color: var(--ink); font-weight: 400; line-height: 1.05; }
  .person-name b { font-weight: 700; }
  .person-title { font-size: 17px; color: var(--orange); line-height: 1.2; }
  .contacts { position: absolute; left: 60px; top: 176px; list-style: none; }
  .contacts li {
    display: flex; align-items: center; gap: 12px;
    font-size: 14px; color: var(--grey-text); height: 26px;
  }
  .contacts li.address { height: 36px; line-height: 1.25; }
  .icon {
    width: 20px; height: 20px; flex: none;
    border: 1.3px solid var(--orange); border-radius: 50%;
    display: flex; align-items: center; justify-content: center;
  }
  .icon svg { width: 11px; height: 11px; fill: var(--orange); }
  .band {
    position: absolute; left: 0; right: 0; bottom: 0; height: 100px;
    background: var(--orange);
  }
  .website {
    position: absolute; left: 60px; bottom: 32px;
    color: #fff; font-size: 18px; letter-spacing: 0.3px;
  }
  .card-back {
    left: 390px; top: 560px; background: var(--orange);
    display: flex; align-items: center; justify-content: center;
  }
  .back-logo { color: var(--ink); font-weight: 700; font-size: 44px; }
</style>
</head>
<body>
  <section class="card card-front">
    <div class="front-logo">Pellor Valley Hospital</div>
    <div class="rule-orange"></div>
    <div class="person">
      <p class="person-name">Dale <b>Hoskin</b></p>
      <p class="person-title">CEO</p>
    </div>
    <div class="rule-black"></div>
    <ul class="contacts">
      <li><span class="icon"><svg viewBox="0 0 12 12"><path d="M2 1h3l1 3-1.5 1a6 6 0 0 0 2.5 2.5L8 6l3 1v3c0 .6-.4 1-1 1C5 11 1 7 1 2c0-.6.4-1 1-1z"/></svg></span>555-321-0147 &amp; Direct xxxxxx</li>
      <li><span class="icon"><svg viewBox="0 0 12 12"><path d="M3 1h6v3H3zM1 5h10v5H9V8H3v2H1zM4 9h4v2H4z"/></svg></span>Fax xxxxx</li>
      <li><span class="icon"><svg viewBox="0 0 12 12"><path d="M1 3h10v6H1zM1.5 3.5 6 7l4.5-3.5" fill="none" stroke="#f0691f" stroke-width="1.2"/></svg></span>dale.hoskin@pellorvh.example</li>
      <li class="address"><span class="icon"><svg viewBox="0 0 12 12"><path d="M6 1a3.5 3.5 0 0 1 3.5 3.5C9.5 7 6 11 6 11S2.5 7 2.5 4.5A3.5 3.5 0 0 1 6 1zm0 2a1.5 1.5 0 1 0 0 3 1.5 1.5 0 0 0 0-3z"/></svg></span><span>382 Wimble Street Box 415<br>Brannock, Westria 76902</span></li>
    </ul>
    <div class="band"></div>
    <p class="website">www.website.com</p>
  </section>

  <section class="card card-back">
    <div class="back-logo">Pellor Valley Hospital</div>
  </section>
</body>
</html>
```